Label for Wines Design

I need a label design for a start-up business that makes grape wines. The label of wine features a picture frame on the edges of the wine bottle label. So each style of wine (red, white, sparkling, rose etc) will feature a different colour. As you can picture there is already a lot going on in this label.

My trademark is 'tamo', means 'Virgin pure love',type of wines: Sauvignon Blanc, Merlot, Pino noir etc. All in Caps, a Juxtaposition of old & modern. Bold & thick letters to grab attention on the wine store shelves. Maybe letter spacing squeezed together as the wine label is only 4inches wide...the text 'tamo' must fit on one line! No Cursive or curvy lines! Colors open to black, green, yellow, purple must be natural colors hues in nature.

New Zealand wines are New worlds wines,green and astringency,unique fruity, just as virgin pure love, is an infatuation, lovesickness, never forget......

Target Market(s)

New Zealand and Asian
food & wine lovers all ages

Industry/Entity Type

Business

Font styles to use
Decorative
Script

Colors

Designer to choose colors to be used in the design.

Requirements
Must have
• Front Label and back label
Nice to have
• Wines-feeling is green and astringency,unique fruity, just as virgin pure love, is an infatuation, lovesickness, never forget......

```html
<!DOCTYPE html>
<html lang="en">
<head>
<meta charset="utf-8">
<title>Tamo Pino Noir – Wine Label</title>
<link rel="stylesheet" href="https://fonts.googleapis.com/css2?family=Almendra:wght@700&family=Roboto:wght@300;500&display=swap">
<style>
  :root {
    --canvas-bg: #f2f1f3;
    --label-paper: #f7f7f8;
    --label-edge: #c9c6cc;
    --frame-violet: #a04bb8;
    --frame-violet-light: #c77ad6;
    --ornament-plum: #6a2a78;
    --ornament-rose: #d9a0a0;
    --band-mauve: #8a5a8e;
    --band-dark: #5e3a66;
    --seal-purple: #4e1a72;
    --seal-ring: #b96ad0;
    --name-white: #ffffff;
    --variety-violet: #b35ac0;
    --vintage-plum: #4a1a5e;
  }
  html, body {
    margin: 0;
    padding: 0;
    width: 1200px;
    height: 1000px;
    overflow: hidden;
    background: var(--canvas-bg);
  }
  .canvas {
    position: relative;
    width: 1200px;
    height: 1000px;
  }
  .wine-label {
    position: absolute;
    left: 205px;
    top: 55px;
    width: 790px;
    height: 890px;
  }
  .brand-name {
    font-family: "Roboto", sans-serif;
    font-weight: 500;
    fill: var(--name-white);
    letter-spacing: 1px;
  }
  .variety-name {
    font-family: "Roboto", sans-serif;
    font-weight: 300;
    fill: var(--variety-violet);
    letter-spacing: 1px;
  }
  .vintage-year {
    font-family: "Almendra", serif;
    font-weight: 700;
    fill: var(--vintage-plum);
  }
</style>
</head>
<body>
<main class="canvas">
  <svg class="wine-label" viewBox="0 0 790 890" xmlns="http://www.w3.org/2000/svg">
    <defs>
      <linearGradient id="band-fill" x1="0" y1="0" x2="1" y2="0">
        <stop offset="0" stop-color="var(--band-mauve)"/>
        <stop offset="0.3" stop-color="var(--band-dark)"/>
        <stop offset="0.7" stop-color="var(--band-dark)"/>
        <stop offset="1" stop-color="var(--band-mauve)"/>
      </linearGradient>
      <radialGradient id="seal-fill" cx="0.5" cy="0.45" r="0.6">
        <stop offset="0" stop-color="#5e2486"/>
        <stop offset="1" stop-color="var(--seal-purple)"/>
      </radialGradient>
      <linearGradient id="flourish-rose" x1="0" y1="0" x2="1" y2="0">
        <stop offset="0" stop-color="var(--ornament-rose)" stop-opacity="0"/>
        <stop offset="0.25" stop-color="var(--ornament-rose)" stop-opacity="0.35"/>
        <stop offset="0.5" stop-color="var(--ornament-rose)" stop-opacity="0.5"/>
        <stop offset="0.75" stop-color="var(--ornament-rose)" stop-opacity="0.35"/>
        <stop offset="1" stop-color="var(--ornament-rose)" stop-opacity="0"/>
      </linearGradient>
      <linearGradient id="filigree-plum" x1="0" y1="0" x2="0" y2="1">
        <stop offset="0" stop-color="var(--ornament-plum)" stop-opacity="0"/>
        <stop offset="0.2" stop-color="var(--ornament-plum)" stop-opacity="0.28"/>
        <stop offset="0.8" stop-color="var(--ornament-plum)" stop-opacity="0.28"/>
        <stop offset="1" stop-color="var(--ornament-plum)" stop-opacity="0"/>
      </linearGradient>
    </defs>

    <!-- label sheet -->
    <rect class="label-sheet" x="2" y="2" width="786" height="886" rx="60" ry="60"
          fill="var(--label-paper)" stroke="var(--label-edge)" stroke-width="2"/>

    <!-- frame: top bracket -->
    <path class="frame-top" d="M89 200 V34 H697 V200" fill="none"
          stroke="var(--frame-violet)" stroke-width="6"/>
    <path class="frame-top-inner" d="M103 170 V48 H683 V170" fill="none"
          stroke="var(--frame-violet-light)" stroke-width="2"/>

    <!-- frame: bottom bracket -->
    <path class="frame-bottom" d="M89 665 V855 H697 V665" fill="none"
          stroke="var(--frame-violet)" stroke-width="6"/>
    <path class="frame-bottom-inner" d="M103 695 V841 H683 V695" fill="none"
          stroke="var(--frame-violet-light)" stroke-width="2"/>

    <!-- corner accents -->
    <g class="corner-dots" fill="var(--ornament-plum)">
      <circle cx="64" cy="42" r="7"/>
      <circle cx="724" cy="42" r="7"/>
      <circle cx="64" cy="848" r="7"/>
      <circle cx="724" cy="848" r="7"/>
    </g>

    <!-- diamonds -->
    <path class="diamond-top" d="M393 64 L409 82 L393 100 L377 82 Z" fill="var(--frame-violet)"/>
    <path class="diamond-bottom" d="M393 764 L409 782 L393 800 L377 782 Z" fill="var(--frame-violet)"/>

    <!-- ornament areas -->
    <ellipse class="ornament-top" cx="393" cy="160" rx="285" ry="42"
             fill="url(#flourish-rose)"
             role="img" aria-label="Rose scrollwork flourish beneath the top diamond"/>
    <ellipse class="ornament-side-left" cx="56" cy="420" rx="30" ry="235"
             fill="url(#filigree-plum)"
             role="img" aria-label="Plum filigree scroll running down the left edge"/>
    <ellipse class="ornament-side-right" cx="732" cy="420" rx="30" ry="235"
             fill="url(#filigree-plum)"
             role="img" aria-label="Plum filigree scroll running down the right edge"/>
    <ellipse class="ornament-bottom" cx="393" cy="712" rx="285" ry="40"
             fill="url(#flourish-rose)"
             role="img" aria-label="Rose scrollwork flourish above the bottom diamond"/>

    <!-- central band -->
    <path class="name-band"
          d="M117 250 H680 Q664 298 680 328 V470 Q664 505 680 550 H117 Q133 505 117 470 V328 Q133 298 117 250 Z"
          fill="url(#band-fill)"/>

    <!-- seal -->
    <circle class="seal-ring" cx="394" cy="400" r="178" fill="var(--label-paper)"/>
    <circle class="seal-ring-line" cx="394" cy="400" r="170" fill="none"
            stroke="var(--seal-ring)" stroke-width="4"/>
    <circle class="seal" cx="394" cy="400" r="158" fill="url(#seal-fill)"/>
    <text class="brand-name" x="394" y="430" font-size="84" text-anchor="middle">TAMO</text>

    <!-- variety -->
    <text class="variety-name" x="394" y="645" font-size="36" text-anchor="middle">PINO NOIR</text>

    <!-- vintage -->
    <text class="vintage-year" x="275" y="762" font-size="60" text-anchor="middle">20</text>
    <text class="vintage-year" x="522" y="762" font-size="60" text-anchor="middle">17</text>
  </svg>
</main>
</body>
</html>
```